Business Card Design

We need a new buisness card designed for a new company in Darwin
We dig trenchs and lay pipes for the communication industry,Electrical industry, Teleco industry,
We also do some concrete works as well,
And small excavation work
Communication
Belvanti Contracting PTY LTD
Pit and Pipe installations
Trenching,Excavations, Concreting ,
civil works, unistrut soloutions ,over thirty years experiance
WHERE NOT FAZED WE WILL LAY ANYTHING
Contact Glen 0491536208 ps
(would like name to stand out somehow in another text or graphic sort of a way am also looking for some sort of slogan) will most likely be a red card with black writing

```html
<!DOCTYPE html>
<html lang="en">
<head>
<meta charset="utf-8">
<title>Belvanti Contracting – Business Card</title>
<link rel="stylesheet" href="https://fonts.googleapis.com/css2?family=Ubuntu:ital,wght@0,400;0,500;0,700;1,700&display=swap">
<style>
  :root {
    --ink: #231f20;
    --red: #e31e24;
    --red-deep: #c8161c;
    --blush: #f3b7a4;
    --white: #ffffff;
    --page: #ffffff;
    --wash: rgba(255, 255, 255, 0.22);
  }
  * { box-sizing: border-box; margin: 0; padding: 0; }
  html, body {
    width: 1200px; height: 1000px; overflow: hidden;
    background: var(--page);
    font-family: "Ubuntu", sans-serif;
    color: var(--ink);
  }
  .canvas { position: relative; width: 1200px; height: 1000px; }

  /* ---------- card ---------- */
  .card {
    position: absolute; left: 150px; top: 60px;
    width: 900px; height: 514px;
    overflow: hidden;
    background: linear-gradient(90deg, var(--white) 0%, var(--white) 12%, var(--blush) 42%, #ea6a55 68%, var(--red) 88%);
    box-shadow: 0 18px 40px rgba(0,0,0,0.18);
  }
  .card__watermark {
    position: absolute; left: 560px; top: 230px;
    width: 290px; height: 290px;
    border-radius: 50%;
    background: var(--wash);
  }
  .brand {
    position: absolute; left: 70px; top: 42px;
    display: flex; align-items: center; gap: 22px;
  }
  .brand__dot {
    width: 92px; height: 92px; border-radius: 50%;
    background: var(--ink); flex: none;
  }
  .brand__name {
    font-weight: 500; font-size: 40px; line-height: 1.08;
    color: var(--ink);
  }
  .ribbon {
    position: absolute; left: 0; top: 178px;
    width: 520px; height: 46px;
  }
  .ribbon__text {
    position: absolute; left: 70px; top: 187px;
    font-size: 24px; font-weight: 500; color: var(--ink);
  }
  .contact {
    position: absolute; left: 40px; top: 262px;
    font-size: 28px; line-height: 1.15; color: var(--ink);
  }
  .contact__name { padding-left: 44px; font-weight: 500; }
  .contact__phone { display: flex; align-items: center; gap: 12px; }
  .contact__phone svg { width: 28px; height: 28px; flex: none; }
  .services {
    position: absolute; left: 560px; top: 150px;
    list-style: none; font-size: 25px; line-height: 1.55; color: var(--ink);
  }
  .services li { display: flex; align-items: center; gap: 12px; }
  .services svg { width: 16px; height: 16px; flex: none; }
  .slogan-band {
    position: absolute; left: 0; bottom: 0;
    width: 100%; height: 96px;
    background: var(--red);
    display: flex; align-items: center; padding-left: 70px;
  }
  .slogan {
    font-weight: 700; font-style: italic; font-size: 33px; color: var(--ink);
  }

  /* ---------- name lockup ---------- */
  .lockup {
    position: absolute; left: 150px; top: 660px;
    display: flex; align-items: center; gap: 40px;
  }
  .lockup__dot {
    width: 190px; height: 190px; border-radius: 50%;
    background: var(--ink); flex: none;
  }
  .lockup__name {
    font-weight: 500; font-size: 62px; line-height: 1.18; color: var(--ink);
  }
</style>
</head>
<body>
<main class="canvas">
  <section class="card" aria-label="Business card front">
    <div class="card__watermark" aria-hidden="true"></div>

    <div class="brand">
      <span class="brand__dot" aria-hidden="true"></span>
      <p class="brand__name">Belvanti<br>Contracting<br>PTY LTD</p>
    </div>

    <svg class="ribbon" viewBox="0 0 520 46" aria-hidden="true">
      <polygon points="0,0 490,0 470,23 520,46 0,46" fill="var(--red)"/>
    </svg>
    <p class="ribbon__text">Over thirty years experiance</p>

    <div class="contact">
      <p class="contact__name">Glen</p>
      <p class="contact__phone">
        <svg viewBox="0 0 24 24" aria-hidden="true">
          <rect x="6" y="2" width="12" height="20" rx="2.5" fill="var(--ink)"/>
          <rect x="8" y="5" width="8" height="11" fill="var(--white)"/>
          <circle cx="12" cy="19" r="1.2" fill="var(--white)"/>
        </svg>
        0 491 536 208
      </p>
    </div>

    <ul class="services">
      <li><svg viewBox="0 0 16 16" aria-hidden="true"><path d="M2 8 L6 12 L14 3" stroke="var(--ink)" stroke-width="3" fill="none"/></svg>Pit and Pipe installations</li>
      <li><svg viewBox="0 0 16 16" aria-hidden="true"><path d="M2 8 L6 12 L14 3" stroke="var(--ink)" stroke-width="3" fill="none"/></svg>Trenching</li>
      <li><svg viewBox="0 0 16 16" aria-hidden="true"><path d="M2 8 L6 12 L14 3" stroke="var(--ink)" stroke-width="3" fill="none"/></svg>Excavations</li>
      <li><svg viewBox="0 0 16 16" aria-hidden="true"><path d="M2 8 L6 12 L14 3" stroke="var(--ink)" stroke-width="3" fill="none"/></svg>Concreting civil works</li>
    </ul>

    <div class="slogan-band">
      <p class="slogan">Where not fazed we will lay anything</p>
    </div>
  </section>

  <section class="lockup" aria-label="Company name lockup">
    <span class="lockup__dot" aria-hidden="true"></span>
    <p class="lockup__name">Belvanti<br>Contracting<br>PTY LTD</p>
  </section>
</main>
</body>
</html>
```